Website for a company offering full serivce charging solutions for electric cars

The company "vorn-werk" (english: "front-works") offering all-in-one-solutions for charging infrastructure for electric mobility.

There are four products:
1- Wallboxes for single-family homes
2- Solutions for property devloper/-management for property parking space
3- All-in-one-charging solution for municipalities/communities
4- Solutions for tourism/hotels/holiday appartments

The Website structure:
1. Main Page
2.1. Product Page Single Homes
2.2. Product Page Property Management / Parking
2.3. Product Page Municipality
2.4. Product Page Tourism
3. Contact Form / Request for information
4. Imprint / Legal

The Website should be built on Wordpress with a powerful possibility to simply add/modify specific landing pages.

We would like you to implement the website later and also maintain it if possible, but we would be able to do minor modifications by ourselfs (for A/B-Testing)

The website should be clear and simple, easy to understand.
Target group is mainly B2C without deeper knowledge of that topic.

It should suggest, that we will provide a very simple way to get the charging infrastructure done.

We need a contact form, maybe we will use Leadmill later.

Attached you will find a draft of the main page and a landing page (for 2.2) - it is just the content, please ignore the design. We would love to let you create a suitable design.
Also you will find some drafts a bit different for the same story.

I added also a few stock photos, but they don't need to be used! If you have better ideas, you are welcome!

Charging/Electric mobility

Sans Serif

• Based on Wordpress, and the designer should be able to implement it on Wordpress on a later step

```html
<!DOCTYPE html>
<html lang="de">
<head>
<meta charset="utf-8">
<title>vorn-werk – Ladelösungen</title>
<link href="https://fonts.googleapis.com/css2?family=Manrope:wght@400;500;600;700&display=swap" rel="stylesheet">
<style>
  :root{
    --navy:#101825;
    --navy-soft:#1c2a44;
    --purple:#7360c1;
    --pink:#f108a0;
    --text:#dfe2ea;
    --line:#1d2638;
    --backdrop:#d3d4d6;
  }
  *{box-sizing:border-box;margin:0;padding:0}
  html,body{width:1200px;height:2900px;overflow:hidden}
  body{background:var(--backdrop);font-family:"Manrope",sans-serif;color:var(--text)}
  a{color:inherit}
  .page{position:absolute;left:0;top:282px;width:1200px;height:2337px;background:var(--navy);overflow:hidden}
  .page > section, .page > header, .page > footer{position:absolute;left:0;width:1200px}

  /* header */
  .site-header{top:0;height:106px;border-bottom:3px solid;border-image:linear-gradient(90deg,var(--pink),var(--purple)) 1}
  .brand{position:absolute;left:161px;top:38px;display:flex;align-items:center;gap:10px;font-weight:600;font-size:21px;color:#fff}
  .brand-dot{width:14px;height:14px;border-radius:50%;background:var(--pink)}
  .nav{position:absolute;left:667px;top:44px;display:flex;gap:31px;font-size:12.5px;color:#fff}
  .nav a{text-decoration:none}
  .btn-outline{position:absolute;border:2px solid var(--pink);border-radius:30px;color:#fff;font-size:12.5px;font-weight:500;display:flex;align-items:center;justify-content:center;text-decoration:none}
  .nav-contact{left:902px;top:32px;width:134px;height:43px}

  /* hero */
  .hero{top:106px;height:601px;border-bottom:1px solid var(--line)}
  .eyebrow{position:absolute;left:161px;top:150px;font-size:11px;letter-spacing:2.5px;color:var(--purple);text-transform:uppercase;font-weight:500}
  .hero-title{position:absolute;left:161px;top:172px;font-size:39px;font-weight:700;color:var(--pink);letter-spacing:-.3px;white-space:nowrap}
  .hero-text{position:absolute;left:163px;top:247px;font-size:13px;line-height:24px;color:var(--text);white-space:nowrap}
  .hero-text p + p{margin-top:10px}
  .hero-text a{color:var(--pink);text-decoration:underline}
  .hero-more{left:163px;top:411px;width:135px;height:43px}
  .hero-circle{position:absolute;left:848px;top:132px;width:246px;height:246px;border-radius:50%;background:var(--navy-soft)}
  .hero-photo{position:absolute;left:583px;top:132px;width:548px;height:330px;border-radius:40% 40% 20% 20%/30% 30% 10% 10%;background:radial-gradient(ellipse at 40% 60%,#f2f2f4 0%,#c9ccd3 45%,rgba(16,24,37,0) 72%),radial-gradient(ellipse at 88% 40%,#b3219c 0%,rgba(16,24,37,0) 30%)}

  /* features */
  .features{top:707px;height:242px;border-bottom:1px solid var(--line)}
  .feature{position:absolute;top:90px;display:flex;gap:16px}
  .feature svg{flex:none}
  .feature h3{font-size:15.5px;font-weight:600;color:#fff;margin-top:-2px}
  .feature p{font-size:10.5px;line-height:21px;color:var(--text);margin-top:3px;white-space:nowrap}

  /* decorative block */
  .accent-block{position:absolute;width:83px;height:83px;background:linear-gradient(135deg,var(--purple) 0%,#9a4ab6 100%)}

  /* pitch */
  .pitch{top:949px;height:263px;border-bottom:1px solid var(--line)}
  .pitch .accent-block{left:161px;top:89px}
  .pitch-text{position:absolute;left:385px;top:88px;font-size:29px;line-height:38px;font-weight:600;color:var(--purple);white-space:nowrap}

  /* offers grid */
  .offers{top:1212px;height:754px;border-bottom:1px solid var(--line)}
  .offer-grid{position:absolute;left:161px;top:88px;width:876px;height:574px;display:grid;grid-template-columns:repeat(3,292px);grid-template-rows:repeat(2,287px)}
  .offer-card{border:1px solid var(--purple);display:flex;flex-direction:column;align-items:center;justify-content:center;text-align:center}
  .offer-card h2{font-size:27px;line-height:34px;font-weight:500}
  .offer-card.pink h2{color:var(--pink)}
  .offer-card.violet h2{color:var(--purple)}
  .offer-card p{font-size:12px;line-height:20px;color:var(--text);margin-top:14px;white-space:nowrap}
  .offer-card .more{margin-top:22px;font-size:10.5px;letter-spacing:.3px;display:flex;align-items:center;gap:6px}
  .offer-card.pink .more{color:var(--purple)}
  .offer-card.violet .more{color:var(--pink)}
  .photo-a{background:linear-gradient(135deg,#3b2a22 0%,#6f5446 40%,#b58fd9 75%,#cfaee8 100%)}
  .photo-b{background:linear-gradient(120deg,#d9dadf 0%,#f4f4f6 35%,#8c8ea0 70%,#e5e5ea 100%)}
  .photo-c{background:linear-gradient(180deg,#e4e4e6 0%,#cfcfd3 55%,#7a5aa8 80%,#5a3f88 100%)}

  /* contact */
  .contact-cta{top:1966px;height:266px}
  .contact-text{position:absolute;left:161px;top:106px;font-size:29px;line-height:38px;font-weight:600;color:var(--purple);white-space:nowrap}
  .contact-text a{text-decoration:underline;text-underline-offset:4px}
  .contact-cta .accent-block{left:956px;top:90px}

  /* footer */
  .site-footer{top:2232px;height:105px;border-top:3px solid;border-image:linear-gradient(90deg,var(--pink),var(--purple)) 1}
  .copyright{position:absolute;left:161px;top:44px;font-size:10px;color:#fff}
  .footer-links span{position:absolute;top:44px;font-size:10px;color:#fff;white-space:nowrap}
  .social{position:absolute;left:964px;top:37px;display:flex;gap:8px}
  .social span{width:29px;height:29px;border-radius:50%;background:linear-gradient(135deg,var(--pink),var(--purple))}
</style>
</head>
<body>
<div class="page">

  <header class="site-header">
    <div class="brand"><span class="brand-dot"></span>vorn-werk.de</div>
    <nav class="nav"><a href="#">Startseite</a><a href="#">Produkte</a><a href="#">Imprint</a></nav>
    <a class="btn-outline nav-contact" href="#">Kontakt</a>
  </header>

  <section class="hero">
    <div class="eyebrow">Willkommen bei Vornwerk</div>
    <h1 class="hero-title">Vorn-werk ist Ihr Partner</h1>
    <div class="hero-text">
      <p>Wenn das Laden nicht nur einfach, sondern die Umsetzung auch<br>aus einer Hand kommen soll</p>
      <p>Wir bieten Lösungen sowohl für <a href="#">Privatkunden, Geschäftskunden</a><br>als auch <a href="#">Kommunen</a> an, die schnell, fair und ohne Eigenleistung<br>zu einer smarten Ladelösung für E-Fahrzeuge kommen möchten.</p>
    </div>
    <a class="btn-outline hero-more" href="#">Weiterlesen</a>
    <div class="hero-circle"></div>
    <div class="hero-photo" role="img" aria-label="Weißes Elektroauto mit einer Frau im pinken Pullover daneben"></div>
  </section>

  <section class="features">
    <div class="feature" style="left:161px">
      <svg width="52" height="52" viewBox="0 0 52 52" fill="none" stroke-width="2" stroke-linecap="round" stroke-linejoin="round">
        <path d="M6 32 L10 20 H36 L40 32" stroke="#7360c1"/>
        <rect x="4" y="32" width="40" height="12" rx="3" stroke="#f108a0"/>
        <circle cx="12" cy="38" r="2.5" stroke="#f108a0"/><circle cx="36" cy="38" r="2.5" stroke="#f108a0"/>
        <path d="M8 44v4M40 44v4" stroke="#7360c1"/>
        <path d="M25 24l-3 6h4l-3 6" stroke="#f108a0"/>
        <path d="M36 20 V10 H46 M46 6 v8" stroke="#7360c1"/>
      </svg>
      <div><h3>Lorem Ipsum</h3><p>Some text filler only for<br>design purposes</p></div>
    </div>
    <div class="feature" style="left:486px">
      <svg width="52" height="58" viewBox="0 0 52 58" fill="none" stroke-width="2" stroke-linecap="round" stroke-linejoin="round">
        <rect x="6" y="6" width="24" height="46" rx="3" stroke="#f108a0"/>
        <rect x="11" y="12" width="14" height="10" stroke="#7360c1"/>
        <path d="M20 28l-4 8h5l-4 8" stroke="#f108a0"/>
        <path d="M2 52h32" stroke="#7360c1"/>
        <path d="M30 34h6v12a4 4 0 0 0 8 0V20" stroke="#7360c1"/>
        <path d="M40 10v6h8v-6M42 10V6M46 10V6" stroke="#f108a0"/>
      </svg>
      <div><h3>Lorem Ipsum</h3><p>Some text filler only for<br>design purposes</p></div>
    </div>
    <div class="feature" style="left:812px">
      <svg width="100" height="56" viewBox="0 0 100 56" fill="none" stroke-width="2" stroke-linecap="round" stroke-linejoin="round">
        <rect x="38" y="4" width="26" height="14" rx="2" stroke="#7360c1"/>
        <path d="M44 8v6M50 8v6M56 8v6M64 11h4" stroke="#7360c1"/>
        <rect x="4" y="24" width="10" height="26" rx="2" stroke="#f108a0"/>
        <path d="M14 34h6v12" stroke="#f108a0"/>
        <path d="M24 48 V40 L32 30 H64 L72 40 H82 V48" stroke="#f108a0"/>
        <circle cx="36" cy="48" r="4" stroke="#7360c1"/><circle cx="70" cy="48" r="4" stroke="#7360c1"/>
        <path d="M2 52h92" stroke="#7360c1"/>
      </svg>
      <div><h3>Lorem Ipsum</h3><p>Some text filler only for<br>design purposes</p></div>
    </div>
  </section>

  <section class="pitch">
    <div class="accent-block" role="img" aria-label="Dekoratives Farbelement"></div>
    <h2 class="pitch-text">Fragen Sie uns nach der auf Ihre individuellen<br>Bedürfnisse zugeschnittenen Lösung</h2>
  </section>

  <section class="offers">
    <div class="offer-grid">
      <div class="photo-a" role="img" aria-label="Frau lädt ein violettes Elektroauto in der Garage"></div>
      <div class="offer-card pink">
        <h2>Als<br>Geschäftskunde</h2>
        <p>Durchführung einer individuellen<br>Bedarfsanalyse inkl. Ermittlung der<br>Anforderungen für</p>
        <div class="more">WEITERLESEN <span>⟶</span></div>
      </div>
      <div class="photo-b" role="img" aria-label="Reihe von Ladesäulen mit angeschlossenen Fahrzeugen"></div>
      <div class="offer-card violet">
        <h2>Als<br>Privatkunde</h2>
        <p>Bestandsanalyse mit umfangreicher<br>Beratung über die Möglichkeiten<br>der Umsetzung</p>
        <div class="more">WEITERLESEN <span>⟶</span></div>
      </div>
      <div class="photo-c" role="img" aria-label="Wallbox an der Wand über einem violetten Auto"></div>
      <div class="offer-card violet">
        <h2>Als<br>Kommune</h2>
        <p>Konzeptionierung möglicher<br>Ladeinfrastrukturen innerhalb<br>Ihrer Gemeinde</p>
        <div class="more">WEITERLESEN <span>⟶</span></div>
      </div>
    </div>
  </section>

  <section class="contact-cta">
    <h2 class="contact-text">Hast du noch eine frage zu vorn-werk?<br><a href="#">Kontaktiere uns jetzt</a></h2>
    <div class="accent-block" role="img" aria-label="Dekoratives Farbelement"></div>
  </section>

  <footer class="site-footer">
    <div class="copyright">© 2022 Vorn-werk GmbH</div>
    <nav class="footer-links">
      <span style="left:402px">AGB</span>
      <span style="left:453px">Datenschutzerklärung</span>
      <span style="left:592px">Impressum</span>
      <span style="left:678px">Kontakt</span>
      <span style="left:747px">Karriere</span>
      <span style="left:817px">FAQs</span>
    </nav>
    <div class="social" aria-label="Soziale Netzwerke"><span></span><span></span><span></span></div>
  </footer>

</div>
</body>
</html>
```